Landing page for Cloud Kitchen buisnies

We need a landing page design fully functional for our Cloud Kitchen company wich is based in Dubai we have a industrial kitchen setup up from where we operate our own online food brands wich are only availble for delivery

Target Market(s)

Its just a company Profile

Requirements
Must have
• Company name is Saffron Lane Group. We have the Logo already

LOGO AND DOMAIN WE HAVE
Nice to have
• Proffesionel high quality design

```html
<!DOCTYPE html>
<html lang="en">
<head>
<meta charset="utf-8">
<title>Saffron Lane Group</title>
<link rel="stylesheet" href="https://fonts.googleapis.com/css2?family=Jost:wght@500;600;700&family=Questrial&display=swap">
<style>
:root{
  --ink:#2b2b2b;
  --night:#161616;
  --gold:#b98a2c;
  --gold-light:#e9c96a;
  --gold-bright:#f1de63;
  --white:#ffffff;
  --muted:#3a3a3a;
  --card-shadow:rgba(0,0,0,.12);
}
*{margin:0;padding:0;box-sizing:border-box}
html,body{width:1200px;height:3097px;overflow:hidden}
body{position:relative;background:var(--white);font-family:"Questrial",sans-serif;color:var(--ink)}
.abs{position:absolute}
.hero{left:0;top:0;width:1200px;height:740px;background:radial-gradient(ellipse at 40% 30%,#3a3a3a 0%,#222 45%,var(--night) 100%)}
.hero-photo{left:665px;top:115px;width:516px;height:516px;border-radius:50%;background:radial-gradient(circle at 50% 45%,#e0642a 0%,#d88a3a 35%,#7a3a1c 62%,#1c1c1c 72%)}
.wordmark{font-family:"Jost",sans-serif;font-weight:600;color:var(--gold);letter-spacing:1px;text-align:center}
.hero-mark{left:172px;top:110px;width:228px;font-size:30px;line-height:1.05}
.hero-mark .dot{display:block;width:60px;height:60px;border:3px solid var(--gold);border-radius:50%;margin:0 auto 14px}
.hero-mark{top:40px}
.pill{display:flex;align-items:center;justify-content:center;border-radius:24px;background:linear-gradient(90deg,#a77a22,var(--gold-light),#a77a22);color:var(--white);font-family:"Jost",sans-serif;font-weight:600;font-size:17px;letter-spacing:.3px}
.btn-signup{left:760px;top:37px;width:126px;height:46px}
.btn-login{left:903px;top:37px;width:126px;height:46px}
.menu-toggle{left:1046px;top:49px;width:36px;height:24px}
.menu-toggle span{display:block;height:3px;background:var(--white);margin-bottom:7.5px}
.social{left:40px;width:12px;height:12px;border-radius:50%;background:var(--white)}
.hero-title{left:171px;top:300px;font-family:"Jost",sans-serif;font-weight:600;font-size:42px;line-height:47px;color:var(--white)}
.hero-title em{font-style:normal;color:var(--gold-light)}
.btn-menu{left:172px;top:410px;width:156px;height:45px}
.section-title{left:0;width:1200px;text-align:center;font-family:"Jost",sans-serif;font-weight:600;font-size:48px;color:var(--ink);letter-spacing:.5px}
.section-title .dot{display:inline-block;width:36px;height:36px;border:3px solid var(--gold);border-radius:50%;vertical-align:-2px;margin:0 12px}
.section-lead{left:0;width:1200px;text-align:center;font-size:14px;line-height:17px;color:var(--muted)}
.dish{top:922px;width:260px;text-align:center}
.dish-photo{width:214px;height:214px;border-radius:50%;margin:0 auto}
.dish h3{font-family:"Jost",sans-serif;font-weight:600;font-size:24px;margin-top:13px;color:var(--ink)}
.dish p{font-size:14px;line-height:16.5px;color:var(--muted);width:210px;margin:8px auto 0}
.dish .price{font-family:"Jost",sans-serif;font-weight:600;font-size:23px;color:var(--gold);margin-top:14px}
.about-title{left:172px;top:1513px;font-family:"Jost",sans-serif;font-weight:600;font-size:46px;line-height:49px;color:var(--white)}
.about-copy{left:172px;top:1627px;width:352px;font-size:14px;line-height:16.2px;text-align:justify;color:var(--white)}
.btn-more{left:172px;top:1843px;width:154px;height:45px}
.about-ring{left:610px;top:1540px;width:470px;height:470px;border-radius:50%;border:9px solid var(--gold);display:flex;align-items:center;justify-content:center}
.about-ring span{font-family:"Jost",sans-serif;font-weight:600;font-size:38px;color:var(--gold-light);text-align:center;line-height:1.15}
.brands{left:172px;top:2298px;width:856px;height:255px;display:flex;gap:2px}
.brand-card{flex:1;background:var(--white);box-shadow:0 0 8px var(--card-shadow);text-align:center;padding-top:52px}
.brand-card .brand-name{font-family:"Jost",sans-serif;font-weight:600;font-size:19px;color:#6c6c6c;display:flex;align-items:center;justify-content:center;gap:8px;height:40px}
.brand-card .brand-name i{width:22px;height:22px;border-radius:50%;background:#8a8a8a;display:block}
.brand-card p{font-size:14px;line-height:16.5px;color:var(--muted);width:170px;margin:30px auto 0}
.footer-title{font-family:"Jost",sans-serif;font-weight:600;font-size:29px;color:var(--ink)}
.contact{left:168px;top:2772px}
.contact-item{display:flex;gap:8px;margin-top:14px;font-size:15px;line-height:17px;color:#4a3a10}
.contact-item svg{flex:none}
.footer-mark{left:460px;top:2760px;width:280px;font-size:40px;color:var(--ink);line-height:1.1}
.footer-mark .dot{display:block;width:110px;height:110px;border:5px solid var(--ink);border-radius:50%;margin:0 auto 16px}
.links{left:836px;top:2772px}
.links ul{list-style:none;margin-top:12px}
.links li{font-size:15px;line-height:21.8px;color:#4a3a10}
.legal{left:0;top:3024px;width:1200px;height:73px;background:var(--night);color:var(--white);font-size:13px;display:flex;align-items:center;justify-content:center}
</style>
</head>
<body>

<header class="hero abs">
  <div class="hero-photo abs" role="img" aria-label="Plate of spaghetti with tomato sauce, basil and grated cheese"></div>
  <div class="hero-mark wordmark abs"><span class="dot"></span>SAFFRON LANE<br>GROUP</div>
  <a class="btn-signup pill abs">SIGN UP</a>
  <a class="btn-login pill abs">LOGIN</a>
  <div class="menu-toggle abs"><span></span><span></span><span></span></div>
  <span class="social abs" style="top:334px"></span>
  <span class="social abs" style="top:373px"></span>
  <span class="social abs" style="top:412px"></span>
  <h1 class="hero-title abs">WELCOME TO<br><em>SAFFRON LANE GROUP</em></h1>
  <a class="btn-menu pill abs">VIEW MENU</a>
</header>

<svg class="abs" style="left:0;top:600px" width="1200" height="142" viewBox="0 600 1200 142">
  <path fill="#fff" d="M0 727 Q40 685 132 679 Q205 680 240 709 Q320 619 445 619 Q580 625 646 697 Q720 640 818 643 Q920 650 986 718 Q1040 689 1094 689 Q1160 690 1200 697 L1200 742 L0 742 Z"/>
</svg>

<h2 class="section-title abs" style="top:772px">OUR<span class="dot"></span>FOOD</h2>
<p class="section-lead abs" style="top:840px">Sed ut perspiciatis unde omnis iste natus error sit voluptatem accusantium doloremque<br>laudantium, totam rem aperiam, eaque ipsa quae ab illo inventore veritati</p>

<article class="dish abs" style="left:149px">
  <div class="dish-photo" role="img" aria-label="Cheese and charcuterie board with pasta" style="background:radial-gradient(circle at 40% 40%,#d8c9a8,#8a6a45 55%,#3b3430)"></div>
  <h3>Sed uerspiciatis</h3>
  <p>Sed ut perspiciatis unde omnis natus error sit voluptatem acc usantdoloremque lauda</p>
  <div class="price">$250.00</div>
</article>
<article class="dish abs" style="left:470px">
  <div class="dish-photo" role="img" aria-label="Quinoa salad bowl with tomatoes and avocado" style="background:radial-gradient(circle at 45% 55%,#d64a32,#8a6b46 50%,#4a3020)"></div>
  <h3>Sed uerspiciatis</h3>
  <p>Sed ut perspiciatis unde omnis natus error sit voluptatem acc usantdoloremque lauda</p>
  <div class="price">$250.00</div>
</article>
<article class="dish abs" style="left:792px">
  <div class="dish-photo" role="img" aria-label="Table of curries, rice and flatbread" style="background:radial-gradient(circle at 50% 50%,#e0962e,#9a5522 50%,#2e2620)"></div>
  <h3>Sed uerspiciatis</h3>
  <p>Sed ut perspiciatis unde omnis natus error sit voluptatem acc usantdoloremque lauda</p>
  <div class="price">$250.00</div>
</article>

<svg class="abs" style="left:0;top:1360px" width="1200" height="750" viewBox="0 1360 1200 750" role="img" aria-label="Dimmed photo of a healthy food bowl">
  <defs>
    <radialGradient id="aboutShade" cx="35%" cy="45%" r="70%">
      <stop offset="0" stop-color="#3b2a22"/>
      <stop offset=".5" stop-color="#241a18"/>
      <stop offset="1" stop-color="#121010"/>
    </radialGradient>
  </defs>
  <path fill="url(#aboutShade)" d="M0 1527 C150 1420 300 1362 400 1365 C600 1372 800 1515 1000 1513 C1100 1512 1170 1488 1200 1470 L1200 1876 C1140 1995 1000 2105 842 2104 C650 2102 550 2000 400 1962 C280 1940 120 1940 0 1996 Z"/>
</svg>
<h2 class="about-title abs">ABOUT SAFFRON<br>LANE GROUP</h2>
<p class="about-copy abs">Sed ut perspiciatis unde omnis iste natus error sit voluptatem accusantium doloremque laudantium, totam rem aperiam, eaque ipsa quae ab illo inventore veritatis et quasi architecto beatae vitae dicta sunt explicabo. Nemo enim ipsam voluptatem quia voluptas sit aspernatur aut odit aut fugit, sed quia consequuntur magni dolores eos qui ratione voluptatem sequi nesciunt. Neque porro quisquam est, qui dolorem ipsum quia dolor sit amet, consectetur, adipisci velit, sed quia non numquam eius modi tempora incidunt ut labore et dolore magnam aliquam quaera</p>
<a class="btn-more pill abs">READ MORE</a>
<div class="about-ring abs"><span>SAFFRON LANE<br>GROUP</span></div>

<h2 class="section-title abs" style="top:2152px">FOOD BRANDS</h2>
<p class="section-lead abs" style="top:2219px">Sed ut perspiciatis unde omnis iste natus error sit voluptatem accusantium doloremque<br>laudantium, totam rem aperiam, eaque ipsa quae ab illo inventore veritati</p>

<section class="brands abs">
  <div class="brand-card"><div class="brand-name"><i></i>Tin Spoon</div><p>Sed ut perspiciatis und eomnis iste natus errorsit voluptatem accu san ium doloremque</p></div>
  <div class="brand-card"><div class="brand-name"><i></i>Copper Pot</div><p>Sed ut perspiciatis und eomnis iste natus errorsit voluptatem accu san ium doloremque</p></div>
  <div class="brand-card"><div class="brand-name"><i></i>Ember Fork</div><p>Sed ut perspiciatis und eomnis iste natus errorsit voluptatem accu san ium doloremque</p></div>
  <div class="brand-card"><div class="brand-name"><i></i>Basil Row</div><p>Sed ut perspiciatis und eomnis iste natus errorsit voluptatem accu san ium doloremque</p></div>
</section>

<svg class="abs" style="left:0;top:2640px" width="1200" height="384" viewBox="0 2640 1200 384">
  <defs>
    <linearGradient id="footerGold" x1="0" y1="0" x2="1" y2="0">
      <stop offset="0" stop-color="#b88a2a"/>
      <stop offset=".45" stop-color="#f1de63"/>
      <stop offset="1" stop-color="#c19a35"/>
    </linearGradient>
  </defs>
  <path fill="url(#footerGold)" d="M0 2676 Q120 2742 240 2657 Q440 2800 634 2651 Q794 2780 956 2663 Q1118 2770 1200 2668 L1200 3024 L0 3024 Z"/>
</svg>

<section class="contact abs">
  <h3 class="footer-title">CONTACT</h3>
  <div class="contact-item"><svg width="36" height="36" viewBox="0 0 36 36"><circle cx="18" cy="18" r="16" fill="none" stroke="#2b2b2b" stroke-width="2"/><path d="M18 9a6 6 0 0 0-6 6c0 5 6 12 6 12s6-7 6-12a6 6 0 0 0-6-6z" fill="none" stroke="#2b2b2b" stroke-width="2"/><circle cx="18" cy="15" r="2" fill="#2b2b2b"/></svg><span>Sed ut peatisunde omnis<br>iste atus error sitvo</span></div>
  <div class="contact-item"><svg width="36" height="36" viewBox="0 0 36 36"><circle cx="18" cy="18" r="16" fill="none" stroke="#2b2b2b" stroke-width="2"/><path d="M12 11l4-1 2 5-2 2c1 2 3 4 5 5l2-2 5 2-1 4c-8 0-15-7-15-15z" fill="#2b2b2b"/></svg><span>Phone:<br>555 018 2047</span></div>
  <div class="contact-item"><svg width="36" height="36" viewBox="0 0 36 36"><circle cx="18" cy="18" r="16" fill="none" stroke="#2b2b2b" stroke-width="2"/><rect x="10" y="12" width="16" height="12" rx="1.5" fill="#2b2b2b"/><path d="M10.5 13l7.5 6 7.5-6" fill="none" stroke="#f1de63" stroke-width="1.5"/></svg><span>Email:<br>hello@saffronlane.example</span></div>
</section>

<div class="footer-mark wordmark abs"><span class="dot"></span>SAFFRON LANE<br>GROUP</div>

<section class="links abs">
  <h3 class="footer-title">LINKS</h3>
  <ul>
    <li>Sed ut peatis</li>
    <li>Eunde omnis iste</li>
    <li>Natus error sitvo</li>
    <li>Eptatem accusa</li>
    <li>Ntium doloremqu</li>
    <li>Kaudantium</li>
    <li>Rtam rem periam</li>
  </ul>
</section>

<footer class="legal abs">© 2020 All Rights are reserved. Privacy &nbsp;|&nbsp; Terms of use</footer>

</body>
</html>
```